Hair Extension Website for my business store.

I need a e-commerce website for my store. Something similar to VORELLA.com
Easy to update. May use WIX or Other platforms. I have my my own logo. It is gold. I’m looking for a website very similar to Vorella.com. The arrangement and all. Very easy to navigate. 5 pages. Over 100 products. Almost the same titles of the products.

Industry/Entity Type

Hair Care Product

Coding

Coded - Design and coding required

Number of Pages Required

5+ page

Font styles to use
Sans Serif

Colors
0255a3
fbed22

Requirements
Must have
• Something similar to Vorella.com

Prefered color purple and gold
Nice to have
• Similar to Vorella.com

Able to have many products.
Should not have
• I want all photos to lopk professional.

```html
<!DOCTYPE html>
<html lang="en">
<head>
<meta charset="utf-8">
<title>Lumea Natural Hair</title>
<link href="https://fonts.googleapis.com/css2?family=Open+Sans:wght@400;600;700&family=Roboto:wght@400;500;700;900&family=Great+Vibes&family=Playfair+Display:ital@1&display=swap" rel="stylesheet">
<style>
:root{
  --pink:#e8398a;
  --gold:#d49b3b;
  --dark:#1b1b1b;
  --text:#444;
  --muted:#888;
  --light:#f4f4f4;
  --line:#e3e3e3;
  --white:#fff;
}
*{box-sizing:border-box;margin:0;padding:0}
html,body{width:1200px;height:4824px;overflow:hidden}
body{position:relative;background:var(--white);font-family:"Open Sans",sans-serif;color:var(--text)}
.abs{position:absolute}
.btn{display:inline-flex;align-items:center;justify-content:center;font:700 10px "Open Sans",sans-serif;text-transform:uppercase;color:var(--white);white-space:nowrap}
.btn-pink{background:var(--pink)}
.btn-dark{background:var(--dark)}
.btn-gold{background:var(--gold)}
.stars{color:var(--gold);font-size:10px;letter-spacing:1px}

/* top bar */
.topbar{top:0;left:0;width:1200px;height:32px;font-size:10px;display:flex;align-items:center}
.topbar .service{position:absolute;left:94px;color:var(--muted)}
.topbar .service b{color:var(--dark);font-weight:600}
.topbar .acct{position:absolute;left:460px;display:flex;gap:26px;font-size:9px;color:var(--dark);font-weight:600}
.topbar .acct span::before{content:"";display:inline-block;width:10px;height:10px;border:1px solid #999;border-radius:50%;margin-right:5px;vertical-align:-2px}
.topbar .lang{position:absolute;left:1018px;font-size:9px;color:var(--dark)}
.topbar .cur{position:absolute;left:1072px;font-size:9px;color:var(--dark)}
.auth{top:40px;left:972px;display:flex;gap:4px}
.auth .btn{height:28px;width:66px;font-weight:400}
.logo{top:42px;left:96px;width:86px;text-align:center;color:var(--gold);font:700 22px "Roboto",sans-serif;line-height:1}
.logo .mark{width:30px;height:30px;border-radius:50%;background:var(--gold);margin:0 auto 4px}
.logo small{display:block;font-size:9px;letter-spacing:1px;font-weight:700}
.nav{top:94px;left:443px;display:flex;gap:28px;font-size:10px;color:var(--dark);text-transform:uppercase}
.nav .active{color:var(--pink)}
.nav-search{top:91px;left:1092px}

/* hero */
.hero{top:122px;left:0;width:1200px;height:477px;background:var(--light)}
.hero-left{left:94px;top:28px;width:382px;height:423px;background:linear-gradient(160deg,#6f8ca3,#33495a)}
.hero-frame{left:170px;top:80px;width:258px;height:318px;border:2px solid var(--pink)}
.hero-left-caption{left:94px;top:320px;width:382px;text-align:center;color:var(--white);font:700 33px "Roboto",sans-serif;line-height:1}
.hero-left-caption small{display:block;font-size:21px;font-weight:500;margin-bottom:6px}
.hero-center{left:510px;top:140px;width:330px;text-align:center;color:var(--dark)}
.hero-center .script{font:italic 26px "Playfair Display",serif}
.hero-center .most{font:700 36px "Roboto",sans-serif;margin-top:8px}
.hero-center .big{font:900 58px "Roboto",sans-serif;line-height:1}
.hero-center .tag{display:inline-block;margin-top:8px;border:1px solid #aaa;padding:5px 14px;font-size:10px;letter-spacing:4px}
.dots{left:660px;top:378px;display:flex;gap:4px}
.dots i{width:5px;height:5px;border-radius:50%;background:var(--dark)}
.dots i:first-child{background:var(--pink)}
.hero-right{left:867px;top:28px;width:239px;height:421px;background:linear-gradient(160deg,#f7f7f7,#5a3c2c)}

/* section heads */
.sec-title{left:0;width:1200px;text-align:center;font:900 36px "Roboto",sans-serif;color:var(--dark)}
.sec-sub{left:0;width:1200px;text-align:center;font-size:12px;color:var(--muted)}
.arrows{display:flex;gap:6px}
.arrows i{width:28px;height:28px;border:1px solid #ccc;border-radius:50%;display:flex;align-items:center;justify-content:center;font-style:normal;font-size:13px;color:var(--dark)}

/* product row */
.prow{left:94px;width:1012px;display:flex;justify-content:space-between}
.pcard{width:247px;position:relative}
.pcard .img{position:relative;height:205px;background:linear-gradient(160deg,#d9d9d9,#3d342f)}
.pcard .img .lbl{position:absolute;left:24px;top:36px;font-size:16px;color:var(--dark)}
.pcard .meta{display:flex;justify-content:space-between;align-items:center;margin-top:16px;font-size:14px;color:var(--dark)}
.pcard .price{color:var(--gold);font-weight:700;font-size:15px;margin-top:4px}
.pcard .foot{display:flex;justify-content:space-between;align-items:center;margin-top:6px}
.pcard .foot .btn{width:90px;height:29px}
.pcard .foot span.review{font-size:10px;color:var(--muted);margin-right:18px}

/* classification */
.grey-band{top:1095px;left:0;width:1200px;height:405px;background:#f7f7f7}
.classify{top:1110px;left:94px;width:239px;height:397px;background:var(--white);border:1px solid var(--line);padding:16px 16px}
.classify h3{font:500 22px "Roboto",sans-serif;color:var(--dark);margin-bottom:10px}
.classify li{list-style:none;height:50px;border-top:1px solid var(--line);display:flex;align-items:center;font-size:12px;color:var(--text)}
.classify li::before{content:"";width:10px;height:22px;background:var(--dark);border-radius:3px 3px 6px 6px;margin:0 14px 0 4px}
.classify li::after{content:"›";margin-left:auto;color:var(--dark)}
.feat-label{top:1106px;left:346px;font-size:17px;color:#999}
.feat-label b{color:var(--dark);font-weight:600}
.fgrid{width:758px;left:348px;display:flex;justify-content:space-between}
.fcard{width:242px;text-align:center;position:relative}
.fcard .img{height:235px;background:linear-gradient(180deg,#e9ecf1,#b4a093)}
.fcard .stars{display:block;margin-top:10px}
.fcard p{font-size:11px;line-height:16px;margin-top:6px;color:var(--text)}
.fcard .price{color:var(--gold);font-size:17px;font-weight:700;margin-top:6px}
.fcard .acts{display:flex;justify-content:center;gap:6px;margin-top:6px}
.fcard .acts .btn{width:90px;height:28px}
.promo-card{top:1543px;left:94px;width:239px;height:458px;background:linear-gradient(180deg,#e6ebf2,#c7a87b)}
.promo-card svg{position:absolute;left:0;bottom:0}
.promo-card .name{position:absolute;left:0;width:239px;top:380px;text-align:center;color:var(--white);font:italic 17px "Playfair Display",serif}
.promo-card .btn{position:absolute;left:72px;top:412px;width:96px;height:30px}
.view-all{top:1958px;left:627px;width:199px;height:42px;font-weight:400}

/* tiles */
.tile{top:2063px;height:212px}
.tile.video{left:94px;width:331px;background:linear-gradient(160deg,#6c6c6c,#2d2d2d)}
.play{position:absolute;left:145px;top:86px;width:40px;height:40px;border-radius:50%;border:2px solid #fff;background:rgba(0,0,0,.3)}
.play::after{content:"";position:absolute;left:15px;top:11px;border-left:12px solid #fff;border-top:8px solid transparent;border-bottom:8px solid transparent}
.tile.sale{color:var(--white);text-align:center}
.tile.sale .kicker{position:absolute;left:0;width:100%;top:54px;font:500 18px "Roboto",sans-serif;letter-spacing:1px;line-height:1}
.tile.sale .word{position:absolute;left:0;width:100%;top:64px;font:400 92px "Great Vibes",cursive;line-height:1.2}
.tile .cart{position:absolute;right:18px;bottom:14px;width:30px;height:30px;border-radius:50%;background:var(--white)}
.tile .cart::after{content:"";position:absolute;left:9px;top:10px;width:12px;height:8px;background:var(--dark);border-radius:0 0 2px 2px}

/* bands */
.band{left:0;width:1200px;height:309px}
.band .title{position:absolute;font:900 52px "Roboto",sans-serif;color:var(--white)}
.band .tag{position:absolute;font:italic 15px "Playfair Display",serif;color:var(--white)}
.band .btn{position:absolute;width:92px;height:30px}

/* tabs */
.tabs{top:2784px;left:0;width:1200px;display:flex;justify-content:center;gap:16px;font-size:11px;color:var(--dark)}
.tabs span+span::before{content:"";display:inline-block;width:6px;height:6px;border-radius:50%;background:var(--pink);margin-right:16px;vertical-align:1px}

/* gallery */
.gallery{top:3590px;left:0;width:1200px;display:grid;grid-template-columns:repeat(4,1fr);gap:5px}
.gallery div{height:244px;background:linear-gradient(160deg,#8e8781,#26211e)}

/* newsletter */
.news{top:4146px;left:0;width:1200px;height:225px;background:var(--light);text-align:center}
.news h2{margin-top:46px;font:900 38px "Roboto",sans-serif;color:var(--dark)}
.news p{margin-top:6px;font-size:14px;letter-spacing:4px;color:#666}
.news .field{position:absolute;left:268px;top:141px;width:662px;height:37px;border:1px solid #ccc;border-radius:20px;background:var(--white);text-align:left}
.news .field .placeholder{position:absolute;left:18px;top:11px;font-size:10px;letter-spacing:2px;color:#999}
.news .field .subscribe{position:absolute;right:3px;top:3px;height:29px;width:98px;border-radius:16px}

/* footer */
.fcol{top:4432px}
.fcol h4{font:500 20px "Roboto",sans-serif;color:var(--dark);margin-bottom:14px}
.fcol li{list-style:none;font-size:12px;line-height:27px;color:#666}
.fcol p{font-size:12px;line-height:19px;color:#666;width:240px}
.social{display:flex;gap:6px;margin-top:8px}
.social i{width:24px;height:24px;border-radius:50%;background:#3b77c9}
.social i:nth-child(3){background:#f0932b}
.social i:nth-child(4){background:#6a6a8c}
.pay{top:4686px;left:0;width:1200px;text-align:center;font:700 19px "Roboto",sans-serif;color:#2b5fa8}
.cards{top:4720px;left:535px;display:flex;gap:4px}
.cards i{width:30px;height:19px;border-radius:3px;background:#ddd}
.cards i:nth-child(1){background:#f2a33a}.cards i:nth-child(2){background:#2b5fa8}.cards i:nth-child(3){background:#4aa3df}.cards i:nth-child(4){background:#bbb}
.copy{top:4754px;left:0;width:1200px;text-align:center;font-size:11px;color:#666}
.copy b{color:var(--gold);font-weight:400}
</style>
</head>
<body>

<header>
  <div class="abs topbar">
    <span class="service">Customer Service <b>+1 (555) 010 4200</b></span>
    <span class="acct"><span>MY ACCOUNT</span><span>WHISHLIST</span><span>MY CART: $0.00</span></span>
    <span class="lang">En ˅</span><span class="cur">$USD ˅</span>
  </div>
  <div class="abs auth"><span class="btn btn-gold">Login</span><span class="btn btn-pink">Sign up</span></div>
  <div class="abs logo"><div class="mark"></div>LUMEA<small>NATURAL HAIR</small></div>
  <nav class="abs nav"><span class="active">Home</span><span>Wave hair</span><span>Hair extension</span><span>Accessories</span><span>Promotion</span><span>Shop by lock</span><span>Contact us</span></nav>
  <svg class="abs nav-search" width="18" height="18" viewBox="0 0 18 18"><circle cx="7.5" cy="7.5" r="5.5" fill="none" stroke="#1b1b1b" stroke-width="2"/><line x1="11.5" y1="11.5" x2="16" y2="16" stroke="#1b1b1b" stroke-width="2"/></svg>
</header>

<section class="abs hero">
  <div class="abs hero-left" role="img" aria-label="Model with curly hair wearing a branded white tee, seated in a studio"></div>
  <div class="abs hero-frame"></div>
  <div class="abs hero-left-caption"><small>LUMEA</small>NATURAL HAIR</div>
  <div class="abs hero-center">
    <div class="script">Bonorum Malorum</div>
    <div class="most">MOST</div>
    <div class="big">BEAUTIFUL</div>
    <div class="tag">FINIBUS BONORUM ET MALORUM</div>
  </div>
  <div class="abs dots"><i></i><i></i><i></i><i></i></div>
  <div class="abs hero-right" role="img" aria-label="Smiling model with long wavy ombre hair"></div>
</section>

<h2 class="abs sec-title" style="top:652px">TOP SALE</h2>
<p class="abs sec-sub" style="top:697px">If you use this site regularly and would like to help keep the site on the Internet</p>
<div class="abs arrows" style="top:712px;left:1044px"><i>‹</i><i>›</i></div>

<div class="abs prow" style="top:752px">
  <div class="pcard"><div class="img" role="img" aria-label="Model with long wavy hair"></div><div class="meta">Fibunas Lorem<span class="stars">★★★★★</span></div><div class="price">$85.00</div><div class="foot"><span class="btn btn-pink">Add to cart</span><span class="review">(65) Review</span></div></div>
  <div class="pcard"><div class="img" role="img" aria-label="Model with shoulder length wavy hair"></div><div class="meta">Fibunas Lorem<span class="stars">★★★★★</span></div><div class="price">$85.00</div><div class="foot"><span class="btn btn-pink">Add to cart</span><span class="review">(65) Review</span></div></div>
  <div class="pcard"><div class="img" role="img" aria-label="Model with short curly hair"></div><div class="meta">Fibunas Lorem<span class="stars">★★★★★</span></div><div class="price">$85.00</div><div class="foot"><span class="btn btn-pink">Add to cart</span><span class="review">(65) Review</span></div></div>
  <div class="pcard"><div class="img" role="img" aria-label="Kinky curly wig on a stand"></div><div class="meta">Fibunas Lorem<span class="stars">★★★★★</span></div><div class="price">$85.00</div><div class="foot"><span class="btn btn-pink">Add to cart</span><span class="review">(65) Review</span></div></div>
</div>

<div class="abs grey-band"></div>
<aside class="abs classify">
  <h3>Main Classification</h3>
  <ul><li>Body wave</li><li>Straight Hair</li><li>Curly Hair</li><li>Deep Wave</li><li>Loose Wave</li><li>Natural Wave</li><li>Water Wave</li></ul>
</aside>
<div class="abs feat-label">Featured <b>Products</b></div>

<div class="abs fgrid" style="top:1148px">
  <div class="fcard"><div class="img" role="img" aria-label="Ombre brown body wave bundle"></div><span class="stars">★★★★★</span><p>Lumea Natural Hair Peruvian Body Wave<br>Lace Closure With 3pcs</p><div class="price">$52.50</div><div class="acts"><span class="btn btn-pink">Add to cart</span><span class="btn btn-dark">Buy now</span></div></div>
  <div class="fcard"><div class="img" role="img" aria-label="Burgundy ombre body wave bundle"></div><span class="stars">★★★★★</span><p>Lumea Natural Hair Peruvian Body Wave<br>Lace Closure With 3pcs</p><div class="price">$52.50</div><div class="acts"><span class="btn btn-pink">Add to cart</span><span class="btn btn-dark">Buy now</span></div></div>
  <div class="fcard"><div class="img" role="img" aria-label="Platinum blonde body wave bundle"></div><span class="stars">★★★★★</span><p>Lumea Natural Hair Peruvian Body Wave<br>Lace Closure With 3pcs</p><div class="price">$52.50</div><div class="acts"><span class="btn btn-pink">Add to cart</span><span class="btn btn-dark">Buy now</span></div></div>
</div>

<div class="abs promo-card" role="img" aria-label="Black to blonde ombre body wave bundle">
  <svg width="239" height="160" viewBox="0 0 239 160"><path d="M0 80 Q150 75 239 0 V160 H0 Z" fill="#e8398a"/></svg>
  <div class="name">Lumea Natural</div>
  <span class="btn btn-dark">Buy now</span>
</div>

<div class="abs fgrid" style="top:1543px">
  <div class="fcard"><div class="img" role="img" aria-label="Two honey blonde body wave bundles"></div><span class="stars">★★★★★</span><p>Lumea Natural Hair Peruvian Body Wave<br>Lace Closure With 3pcs</p><div class="price">$52.50</div><div class="acts"><span class="btn btn-pink">Add to cart</span><span class="btn btn-dark">Buy now</span></div></div>
  <div class="fcard"><div class="img" role="img" aria-label="Black to golden ombre body wave bundle"></div><span class="stars">★★★★★</span><p>Lumea Natural Hair Peruvian Body Wave<br>Lace Closure With 3pcs</p><div class="price">$52.50</div><div class="acts"><span class="btn btn-pink">Add to cart</span><span class="btn btn-dark">Buy now</span></div></div>
  <div class="fcard"><div class="img" role="img" aria-label="Grey ombre body wave bundle" style="background:linear-gradient(180deg,#eef0f3,#9d93a6)"></div><span class="abs" style="left:38px;top:6px;font-size:18px;color:#333">Grey</span><span class="stars">★★★★★</span><p>Lumea Natural Hair Peruvian Body Wave<br>Lace Closure With 3pcs</p><div class="price">$52.50</div><div class="acts"><span class="btn btn-pink">Add to cart</span><span class="btn btn-dark">Buy now</span></div></div>
</div>
<span class="abs btn btn-gold view-all">View all products</span>

<div class="abs tile video" role="img" aria-label="Video still of a model in a white studio"><span class="play"></span></div>
<div class="abs tile sale" style="left:434px;width:332px;background:var(--gold)"><span class="kicker">CLEARENCE</span><span class="word">Sale</span><span class="cart"></span></div>
<div class="abs tile sale" style="left:773px;width:333px;background:var(--pink)"><span class="kicker">CLEARENCE</span><span class="word">Sale</span><span class="cart"></span></div>

<section class="abs band" style="top:2336px">
  <svg class="abs" style="left:0;top:0" width="1200" height="309" viewBox="0 0 1200 309">
    <defs><linearGradient id="bs" x1="0" y1="0" x2="1" y2="1"><stop offset="0" stop-color="#e9e9e9"/><stop offset="1" stop-color="#9c9a98"/></linearGradient></defs>
    <rect width="1200" height="309" fill="#d49b3b"/>
    <path d="M510 0 Q540 240 850 309 H1200 V0 Z" fill="url(#bs)"/>
  </svg>
  <div class="abs" style="left:720px;top:0;width:420px;height:309px" role="img" aria-label="Model in a branded tee leaning on a white brick wall"></div>
  <div class="title" style="left:92px;top:82px">BEAUTY SERIES</div>
  <div class="tag" style="left:138px;top:152px">Sed ut perspiciatis unde omnis iste natus error</div>
  <span class="btn btn-dark" style="left:253px;top:185px">Buy now</span>
</section>

<h2 class="abs sec-title" style="top:2698px">BEST SELLER</h2>
<p class="abs sec-sub" style="top:2743px">If you use this site regularly and would like to help keep the site on the Internet</p>
<div class="abs tabs"><span>Bob Wig</span><span>Body Wave</span><span>Curly Hair</span><span>kinky Curly</span><span>Water Wave</span><span>Straight Hair</span></div>
<div class="abs arrows" style="top:2809px;left:94px"><i>‹</i><i>›</i></div>

<div class="abs prow" style="top:2859px">
  <div class="pcard"><div class="img" role="img" aria-label="Water wave bundle" style="background:linear-gradient(160deg,#fafafa,#222)"><span class="lbl" style="font-size:13px">Water Wave</span></div><div class="meta">Fibunas Lorem<span class="stars">★★★★★</span></div><div class="price">$85.00</div><div class="foot"><span class="btn btn-pink">Add to cart</span><span class="review">(65) Review</span></div></div>
  <div class="pcard"><div class="img" role="img" aria-label="Straight hair bundle" style="background:linear-gradient(160deg,#f0f2f6,#222)"><span class="lbl" style="font-size:20px;top:48px">Straight</span></div><div class="meta">Fibunas Lorem<span class="stars">★★★★★</span></div><div class="price">$85.00</div><div class="foot"><span class="btn btn-pink">Add to cart</span><span class="review">(65) Review</span></div></div>
  <div class="pcard"><div class="img" role="img" aria-label="Deep wave bundle" style="background:linear-gradient(160deg,#fafafa,#222)"><span class="lbl" style="left:140px;top:6px">Deep Wave</span></div><div class="meta">Fibunas Lorem<span class="stars">★★★★★</span></div><div class="price">$85.00</div><div class="foot"><span class="btn btn-pink">Add to cart</span><span class="review">(65) Review</span></div></div>
  <div class="pcard"><div class="img" role="img" aria-label="Pink ombre body wave bundle" style="background:linear-gradient(160deg,#f3f3f3,#e39aa8)"></div><div class="meta">Fibunas Lorem<span class="stars">★★★★★</span></div><div class="price">$85.00</div><div class="foot"><span class="btn btn-pink">Add to cart</span><span class="review">(65) Review</span></div></div>
</div>

<section class="abs band" style="top:3220px">
  <svg class="abs" style="left:0;top:0" width="1200" height="309" viewBox="0 0 1200 309">
    <defs><linearGradient id="fl" x1="0" y1="0" x2="1" y2="1"><stop offset="0" stop-color="#e8e8e8"/><stop offset="1" stop-color="#8f8c8a"/></linearGradient></defs>
    <rect width="1200" height="309" fill="url(#fl)"/>
    <path d="M430 309 Q520 80 780 0 H1200 V309 Z" fill="#d49b3b"/>
  </svg>
  <div class="abs" style="left:200px;top:0;width:260px;height:309px" role="img" aria-label="Model with curly hair in a branded tee in a bright room"></div>
  <div class="title" style="left:695px;top:98px">FINIBUS LOREM</div>
  <div class="tag" style="left:744px;top:166px">Sed ut perspiciatis unde omnis iste natus error</div>
  <span class="btn btn-dark" style="left:857px;top:199px">Buy now</span>
</section>

<div class="abs gallery">
  <div role="img" aria-label="Deep curly wig"></div>
  <div role="img" aria-label="Curly wig in a salon"></div>
  <div role="img" aria-label="Kinky straight hair from behind"></div>
  <div role="img" aria-label="Row of black hair bundles"></div>
  <div role="img" aria-label="Grey, pink and blonde bundles" style="background:linear-gradient(160deg,#d8dbe3,#e2a6b1)"></div>
  <div role="img" aria-label="Model with long wavy hair"></div>
  <div role="img" aria-label="Model in a branded tee by a brick wall" style="background:linear-gradient(160deg,#eeeeee,#8b8784)"></div>
  <div role="img" aria-label="Smiling model with long wavy hair" style="background:linear-gradient(160deg,#3c5d9a,#2a1d18)"></div>
</div>

<section class="abs news">
  <h2>NEWSLETTER</h2>
  <p>SUBSCRIBE TO GET THE LATEST PROMOTION INFO</p>
  <div class="field"><span class="placeholder">✉ YOUR EMAIL:</span><span class="btn btn-pink subscribe">Subscribe</span></div>
</section>

<footer>
  <div class="abs fcol" style="left:94px"><h4>COMPANY</h4><ul><li>Home</li><li>Wave hair</li><li>Hair Extension</li><li>Accessories</li><li>Promotion</li><li>Shop by lock</li><li>Contact us</li></ul></div>
  <div class="abs fcol" style="left:285px"><h4>CATEGORY</h4><ul><li>Bob Wig</li><li>Body Wave</li><li>Curly Hair</li><li>kinky Curly</li><li>Water Wave</li><li>Straight Hair</li></ul></div>
  <div class="abs fcol" style="left:472px"><h4>CLASSIFICATION</h4><ul><li>Body wave</li><li>straight hair</li><li>curly hair</li><li>Deep wave</li><li>Loose wave</li><li>Natural wave</li><li>Water wave</li></ul></div>
  <div class="abs fcol" style="left:706px"><h4>MORE INFO</h4><ul><li>Shipping Order</li><li>Track My Oreder</li><li>My Cart</li><li>Whislist</li><li>My Account</li><li>Return Policy</li><li>Privacy Policy</li></ul></div>
  <div class="abs fcol" style="left:878px"><h4>JOIN US ON PICTORA</h4><p>At vero eos et accusamus et iusto odio dignissimos ducimus qui blanditiis praesentium voluptatum</p><h4 style="margin:22px 0 0">FOLLOW US</h4><div class="social"><i></i><i></i><i></i><i></i></div></div>
  <div class="abs pay">PayLoop</div>
  <div class="abs cards"><i></i><i></i><i></i><i></i></div>
  <div class="abs copy">COPYRIGHT © 2020 <b>LUMEA NATURAL HAIR</b>. ALL RIGHTS RESERVED.</div>
</footer>

</body>
</html>
```